Simple design for eCommerce retailer of Custom Cut Mirror Frames

We need a fresh design for our eCommerce store. Currently, we need a design for each page on the existing site.

Here is the site as it stands right now: glassvela.com

Here is a competitor site that we like. The owner really likes the block look for the home page: framorly.com

Here is a video we would like to feature: https://videohost.example/v/Kp7rTq2LmXa

Here is the color palate, emphasis on the green and purple: https://palettes.example/quiet-bay-theme-48271953/?showPublished=true

Here is an example of a landing page we are currently using: https://glassvela.com/lander-10-off-install/

Font for the site should be the google font Lato

Home page should include the following sections/blocks:

How it works
Shop now
Testimonials
Featured Products
Before and After Gallery
Updates

My team has been slow getting back to me with feedback. I'm pushing them to speed their process up.

Target Market(s)

Women, Ages 35-65+

Number of Pages Required

5+ page

Font styles to use
Sans Serif

Requirements
Must have
• -Before and after gallery
• -Star ratings
• -eCommerce look and feel
• -Info about being able to order free samples
• -Language from the checkmarks on the landing page
• -sleek product page
• -home page should be have a very modern design feel
Should not have
• Product Prices...the user has to use the calculator to determine the price of their purchase.
• Sliders

```html
<!DOCTYPE html>
<html lang="en">
<head>
<meta charset="utf-8">
<title>GlassVela – Custom Cut Mirror Frames</title>
<link href="https://fonts.googleapis.com/css2?family=Lato:ital,wght@0,400;0,700;0,900;1,400&family=Libre+Baskerville:ital,wght@0,400;1,400&display=swap" rel="stylesheet">
<style>
:root{
  --teal:#8dbdbc;
  --teal-deep:#7aaead;
  --purple:#b993cb;
  --purple-soft:#c6a9d4;
  --ink:#3a3a3a;
  --muted:#8a8a8a;
  --line:#d8d8d8;
  --band:#f1f1f1;
  --star:#f2a91f;
  --footer:#23262f;
  --footer-text:#a5a9b3;
  --white:#ffffff;
}
*{box-sizing:border-box;margin:0;padding:0}
html,body{width:1200px;height:4665px;overflow:hidden;background:var(--white)}
body{position:relative;font-family:"Lato",sans-serif;color:var(--ink)}
.abs{position:absolute}

/* header */
.site-header{position:absolute;left:0;top:0;width:1200px;height:161px;background:var(--white)}
.account-icon{left:56px;top:38px}
.brand{position:absolute;left:0;width:1200px;top:30px;display:flex;justify-content:center;align-items:center;gap:10px}
.brand-mark{width:14px;height:14px;background:var(--purple)}
.brand-name{font-family:"Lato",sans-serif;font-weight:700;font-size:26px;color:var(--teal-deep);letter-spacing:.5px}
.header-phone{left:928px;top:46px;font-size:13px;color:var(--ink);display:flex;gap:7px;align-items:center}
.cart-icon{left:1082px;top:40px}
.main-nav{position:absolute;left:0;top:112px;width:1200px;height:36px;border-top:1px solid #ececec;border-bottom:1px solid #ececec;display:flex;justify-content:center;gap:46px;align-items:center;font-size:12px;font-weight:700;letter-spacing:.4px}
.main-nav span::after{content:"";display:inline-block;width:5px;height:5px;border-right:1px solid var(--muted);border-bottom:1px solid var(--muted);transform:rotate(45deg);margin-left:7px;position:relative;top:-3px}
.main-nav span.plain::after{display:none}

/* hero */
.hero{left:0;top:161px;width:1200px;height:412px;background:linear-gradient(100deg,#5a4730 0%,#b09a78 28%,#d8c7a8 48%,#8a6e4f 70%,#3a2c22 100%)}
.hero-frame{left:257px;top:241px;width:509px;height:258px;border:2px solid rgba(255,255,255,.9)}
.hero-title{left:354px;top:326px;white-space:nowrap;font-family:"Libre Baskerville",serif;font-style:italic;font-size:27px;color:var(--white);text-shadow:0 1px 6px rgba(0,0,0,.35)}
.hero-sub{left:500px;top:376px;width:300px;text-align:center;white-space:nowrap;font-size:14px;color:var(--white)}
.pill{display:inline-block;background:var(--white);color:var(--ink);border-radius:20px;font-size:11px;font-weight:700;letter-spacing:.5px;padding:10px 26px}
.hero-btn{left:540px;top:410px}
.samples-badge{left:920px;top:190px;width:190px;height:190px;border-radius:50%;background:var(--purple-soft);border:3px solid rgba(255,255,255,.6);color:var(--white);text-align:center;padding-top:40px}
.samples-badge .small{font-size:14px}
.samples-badge .big{font-size:30px;font-weight:900;line-height:32px}
.samples-badge .tail{font-size:12px;margin-top:4px}

/* section titles */
.section-title{position:absolute;left:0;width:1200px;display:flex;justify-content:center;align-items:center;gap:18px;font-family:"Libre Baskerville",serif;font-size:19px;font-weight:400;color:var(--ink)}
.section-title::before,.section-title::after{content:"";width:80px;height:1px;background:#9a9a9a}

/* features */
.features{left:0;top:660px;width:1200px;height:353px;background:var(--band)}
.feature{position:absolute;font-size:13px;color:#555;display:flex;align-items:center;gap:12px}
.feature.left{right:740px}
.feature.right{left:760px}
.tick{width:22px;height:22px;flex:none}
.quote-card{left:460px;top:660px;width:270px;height:353px;background:var(--teal);color:var(--white);text-align:center;padding:58px 28px 0}
.quote-card p{font-size:13px;line-height:19px;font-weight:700}
.quote-card .who{font-size:12px;margin-top:14px}
.quote-marks{right:34px;top:16px;font-family:"Libre Baskerville",serif;font-size:90px;line-height:90px;color:rgba(255,255,255,.35)}
.stars{color:var(--star);letter-spacing:2px}
.quote-card .stars{font-size:14px;margin-top:8px}
.btn-purple{display:inline-block;background:var(--purple);color:var(--white);font-size:11px;font-weight:700;letter-spacing:.5px;padding:9px 16px}
.quote-card .btn-purple{margin-top:18px}

/* video */
.video{left:80px;top:1113px;width:1040px;height:537px;background:linear-gradient(110deg,#9aa3b2 0%,#d8dbe2 22%,#3b3a52 45%,#4b3f8c 62%,#c9bcc0 85%,#e3d6d2 100%)}
.video-frame{left:380px;top:1238px;width:380px;height:274px;border:2px solid rgba(255,255,255,.9);text-align:center;color:var(--white)}
.video-frame .title{font-family:"Libre Baskerville",serif;font-style:italic;font-size:24px;margin-top:96px;white-space:nowrap;text-shadow:0 1px 6px rgba(0,0,0,.4)}
.video-frame .pill{margin-top:18px}
.play{left:1027px;top:1571px}

/* products */
.product{position:absolute;width:232px}
.product .swatch{width:232px;height:318px}
.product .name{font-size:11px;color:#444;margin-top:22px}
.product .stars{font-size:12px;margin-top:2px}

/* gallery */
.gallery{left:80px;top:2696px;width:1040px;height:692px;background:linear-gradient(90deg,#3c3c40 0%,#6a6a6d 35%,#4d4e52 70%,#2d2e31 100%)}
.gallery-number{left:106px;top:2905px;color:var(--white);font-size:44px;font-weight:900}
.gallery-caption{left:106px;top:2965px;color:var(--white);font-size:13px;line-height:17px}
.shot{position:absolute;top:2767px;height:489px;border:6px solid var(--white);box-shadow:0 6px 20px rgba(0,0,0,.45)}
.shot-before{left:200px;width:462px;background:linear-gradient(160deg,#c9a493 0%,#e6d2c3 40%,#b39682 70%,#7c6a5b 100%)}
.shot-after{left:666px;width:452px;background:linear-gradient(160deg,#d0ab99 0%,#eadbcd 40%,#b79a86 70%,#81705f 100%)}
.shot-label{left:216px;top:2780px;color:var(--white);font-size:20px;background:rgba(0,0,0,.35);padding:2px 6px}
.round-arrow{position:absolute;width:34px;height:34px;border-radius:50%;background:var(--white)}
.counter{left:290px;top:3302px;color:var(--white);font-size:14px;font-weight:700}
.progress{left:200px;top:3330px;width:820px;height:2px;background:rgba(255,255,255,.3)}
.progress i{display:block;width:55px;height:2px;background:var(--white)}
.mini-arrow{position:absolute;width:24px;height:24px;border-radius:50%;border:1px solid rgba(255,255,255,.7)}

/* satisfaction */
.guarantee{left:80px;top:3420px;width:1040px;height:334px;background:var(--teal)}
.guarantee-inner{left:106px;top:3446px;width:988px;height:282px;border:2px solid var(--white);text-align:center}
.guarantee-inner h2{font-family:"Libre Baskerville",serif;font-weight:400;color:var(--white);font-size:30px;letter-spacing:1px;margin-top:86px}
.guarantee-inner .btn-purple{font-size:22px;padding:8px 22px;margin-top:38px}

/* testimonials */
.stories-title{left:0;top:3802px;width:1200px;text-align:center;font-family:"Libre Baskerville",serif;font-weight:400;font-size:22px}
.stories-sub{left:0;top:3842px;width:1200px;display:flex;justify-content:center;align-items:center;gap:16px;font-size:14px;color:var(--muted)}
.stories-sub::before,.stories-sub::after{content:"";width:90px;height:1px;background:#bdbdbd}
.avatar{left:556px;top:3886px;width:90px;height:90px;border-radius:50%;background:radial-gradient(circle at 50% 40%,#d7c7b3,#8fb6cf);border:3px solid #e7eef2}
.testimonial-text{left:130px;top:4022px;width:940px;text-align:center;font-size:14.5px;line-height:23px;color:#555}
.testimonial-stars{left:0;top:4100px;width:1200px;text-align:center;font-size:16px}
.testimonial-name{left:0;top:4134px;width:1200px;text-align:center;font-size:13px;color:#555}

/* footer */
.site-footer{left:0;top:4198px;width:1200px;height:467px;background:var(--footer);color:var(--footer-text);font-size:12px}
.footer-col{position:absolute;top:82px}
.footer-col h4{color:var(--white);font-size:14px;letter-spacing:.6px;font-weight:900;margin-bottom:28px}
.contact-row{display:flex;gap:10px;margin-bottom:14px;line-height:17px}
.contact-row a{color:#7fb6d8;text-decoration:none}
.post{display:flex;gap:12px;margin-bottom:18px}
.post-dot{width:36px;height:36px;border-radius:50%;background:#3a3e4a;flex:none}
.post p{line-height:16px}
.post .date{color:#58a6d3}
.field{width:238px;height:36px;border:1px solid #4a4e5a;color:#8c909a;font-size:11px;padding:10px;margin-bottom:12px}
.field.area{height:90px}
.send{width:238px;height:32px;background:#3b3f4b;color:#c9ccd3;font-size:11px;font-weight:700;text-align:center;line-height:32px;letter-spacing:.6px}
.thumbs{display:grid;grid-template-columns:repeat(3,66px);gap:8px}
.thumbs span{width:66px;height:66px;background:#3b3f4b}
</style>
</head>
<body>

<header class="site-header">
  <svg class="abs account-icon" width="20" height="22" viewBox="0 0 20 22" fill="none" stroke="#777" stroke-width="1.5"><circle cx="10" cy="6" r="5"/><path d="M1 21c1-5 5-7 9-7s8 2 9 7"/></svg>
  <div class="brand"><span class="brand-mark"></span><span class="brand-name">GlassVela</span></div>
  <div class="abs header-phone">
    <svg width="12" height="12" viewBox="0 0 24 24" fill="#666"><path d="M6.6 10.8a15 15 0 0 0 6.6 6.6l2.2-2.2c.3-.3.7-.4 1-.2 1.1.4 2.3.6 3.6.6.6 0 1 .4 1 1V20c0 .6-.4 1-1 1C10.6 21 3 13.4 3 4c0-.6.4-1 1-1h3.5c.6 0 1 .4 1 1 0 1.3.2 2.5.6 3.6.1.3 0 .7-.2 1z"/></svg>
    (555) 014-2290
  </div>
  <svg class="abs cart-icon" width="28" height="24" viewBox="0 0 28 24" fill="none" stroke="#555" stroke-width="1.6"><path d="M1 2h4l3 13h14l3-9H7"/><circle cx="10" cy="20" r="2"/><circle cx="20" cy="20" r="2"/><circle cx="23" cy="4" r="4" fill="var(--purple)" stroke="none"/></svg>
  <nav class="main-nav">
    <span class="plain">HOME</span><span>SHOP MIRROR FRAMES</span><span>CUSTOM FRAMED MIRRORS</span><span>HOW IT WORKS</span><span class="plain">BEFORE AND AFTER GALLERY</span>
  </nav>
</header>

<section class="abs hero" role="img" aria-label="Photo of a bathroom mirror finished with a dark custom cut frame"></section>
<div class="abs hero-frame"></div>
<h1 class="abs hero-title" style="font-weight:400">Frame Any Mirror In Your House</h1>
<div class="abs hero-sub">with an elegant custom cut frame</div>
<span class="abs pill hero-btn">SHOP NOW</span>
<div class="abs samples-badge">
  <div class="small">Get up to 12</div>
  <div class="big">FREE<br>SAMPLES</div>
  <div class="tail">Mailed to your door</div>
</div>

<h2 class="section-title" style="top:598px">Quick, Easy, and Affordable</h2>

<section class="abs features">
  <div class="feature left" style="top:66px">DIY mirror framing kit <svg class="tick" viewBox="0 0 22 22" fill="none" stroke="var(--purple)" stroke-width="1.4"><circle cx="11" cy="11" r="10"/><path d="M6.5 11.5l3 3 6-6.5"/></svg></div>
  <div class="feature left" style="top:136px">Install with mirror still on wall <svg class="tick" viewBox="0 0 22 22" fill="none" stroke="var(--purple)" stroke-width="1.4"><circle cx="11" cy="11" r="10"/><path d="M6.5 11.5l3 3 6-6.5"/></svg></div>
  <div class="feature left" style="top:190px">Style selections to match any home decor <svg class="tick" viewBox="0 0 22 22" fill="none" stroke="var(--purple)" stroke-width="1.4"><circle cx="11" cy="11" r="10"/><path d="M6.5 11.5l3 3 6-6.5"/></svg></div>
  <div class="feature left" style="top:242px">DIY install within minutes <svg class="tick" viewBox="0 0 22 22" fill="none" stroke="var(--purple)" stroke-width="1.4"><circle cx="11" cy="11" r="10"/><path d="M6.5 11.5l3 3 6-6.5"/></svg></div>

  <div class="feature right" style="top:66px"><svg class="tick" viewBox="0 0 22 22" fill="none" stroke="var(--purple)" stroke-width="1.4"><circle cx="11" cy="11" r="10"/><path d="M6.5 11.5l3 3 6-6.5"/></svg> Guaranteed to fit any mirror, any size</div>
  <div class="feature right" style="top:136px"><svg class="tick" viewBox="0 0 22 22" fill="none" stroke="var(--purple)" stroke-width="1.4"><circle cx="11" cy="11" r="10"/><path d="M6.5 11.5l3 3 6-6.5"/></svg> Extends beyond mirror to hide ugly edges</div>
  <div class="feature right" style="top:190px"><svg class="tick" viewBox="0 0 22 22" fill="none" stroke="var(--purple)" stroke-width="1.4"><circle cx="11" cy="11" r="10"/><path d="M6.5 11.5l3 3 6-6.5"/></svg> Beveled Mirrors? No problem!</div>
  <div class="feature right" style="top:242px"><svg class="tick" viewBox="0 0 22 22" fill="none" stroke="var(--purple)" stroke-width="1.4"><circle cx="11" cy="11" r="10"/><path d="M6.5 11.5l3 3 6-6.5"/></svg> Outstanding customer support</div>
</section>

<aside class="abs quote-card">
  <div class="abs quote-marks">&#8221;</div>
  <p>Great Product and Great Service! Adding frames to our mirrors made all the difference in how the master bath looks. You can't beat GlassVela for the money!</p>
  <div class="who">Dana R., Harbor Point, CA</div>
  <div class="stars">★★★★★</div>
  <span class="btn-purple">GET FREE SAMPLE CODE</span>
</aside>

<h2 class="section-title" style="top:1049px">How It Works</h2>

<section class="abs video" role="img" aria-label="Video still of a woman fitting a dark frame onto a bathroom mirror"></section>
<div class="abs video-frame">
  <div class="title">See How Easy It Is To Install</div>
  <span class="pill">WATCH</span>
</div>
<svg class="abs play" width="56" height="56" viewBox="0 0 56 56"><circle cx="28" cy="28" r="26" fill="none" stroke="#fff" stroke-width="3"/><path d="M22 17l17 11-17 11z" fill="#fff"/></svg>

<h2 class="section-title" style="top:1692px">Fan Favorites</h2>

<div class="product" style="left:97px;top:1763px"><div class="swatch" role="img" aria-label="Silver frame sample" style="background:linear-gradient(135deg,#6f6e67,#b9b6a8 45%,#e9e4d6 70%)"></div><div class="name">Versatile Look</div><div class="stars">★★★★★</div></div>
<div class="product" style="left:347px;top:1763px"><div class="swatch" role="img" aria-label="Bronze frame sample" style="background:linear-gradient(135deg,#5a3a22,#a67a52 45%,#ece6da 70%)"></div><div class="name">Versatile Look</div><div class="stars">★★★★★</div></div>
<div class="product" style="left:605px;top:1763px"><div class="swatch" role="img" aria-label="Black frame sample" style="background:linear-gradient(135deg,#1d1d1f,#5a5b5f 45%,#e6e4df 70%)"></div><div class="name">Versatile Look</div><div class="stars">★★★★★</div></div>
<div class="product" style="left:856px;top:1763px"><div class="swatch" role="img" aria-label="Copper frame sample" style="background:linear-gradient(135deg,#6e3a1c,#b36a3a 45%,#efe9dd 70%)"></div><div class="name">Versatile Look</div><div class="stars">★★★★★</div></div>

<div class="product" style="left:97px;top:2210px"><div class="swatch" role="img" aria-label="Espresso frame sample" style="background:linear-gradient(135deg,#2a1d16,#4b3528 45%,#efeae0 70%)"></div><div class="name">Versatile Look</div><div class="stars">★★★★★</div></div>
<div class="product" style="left:347px;top:2210px"><div class="swatch" role="img" aria-label="Cherry frame sample" style="background:linear-gradient(135deg,#4a2414,#8a4a26 45%,#efe7db 70%)"></div><div class="name">Versatile Look</div><div class="stars">★★★★★</div></div>
<div class="product" style="left:605px;top:2210px"><div class="swatch" role="img" aria-label="Ivory frame sample" style="background:linear-gradient(135deg,#cfcfcc,#f2f1ee 45%,#e0ddd6 70%)"></div><div class="name">Versatile Look</div><div class="stars">★★★★★</div></div>
<div class="product" style="left:856px;top:2210px"><div class="swatch" role="img" aria-label="Antique copper frame sample" style="background:linear-gradient(135deg,#5b2d14,#a4602f 45%,#f0eadf 70%)"></div><div class="name">Versatile Look</div><div class="stars">★★★★★</div></div>

<h2 class="section-title" style="top:2644px">Before And After Gallery</h2>

<section class="abs gallery" role="img" aria-label="Dimmed bathroom photo behind the gallery"></section>
<div class="abs gallery-number">06</div>
<div class="abs gallery-caption">ASTER<br>IN IVORY</div>
<div class="shot shot-before" role="img" aria-label="Bathroom vanity mirror before framing"></div>
<div class="shot shot-after" role="img" aria-label="Same bathroom mirror after adding an ivory frame"></div>
<div class="abs shot-label">ASTER IN IVORY</div>
<div class="round-arrow" style="left:612px;top:3216px"><svg width="34" height="34" viewBox="0 0 34 34"><path d="M19 11l-6 6 6 6" fill="none" stroke="#333" stroke-width="2"/></svg></div>
<div class="round-arrow" style="left:664px;top:3216px"><svg width="34" height="34" viewBox="0 0 34 34"><path d="M15 11l6 6-6 6" fill="none" stroke="#333" stroke-width="2"/></svg></div>
<div class="abs counter">06 / 96</div>
<div class="abs progress"><i></i></div>
<div class="mini-arrow" style="left:107px;top:3340px"><svg width="22" height="22" viewBox="0 0 22 22"><path d="M13 7l-4 4 4 4" fill="none" stroke="#fff" stroke-width="1.5"/></svg></div>
<div class="mini-arrow" style="left:139px;top:3340px"><svg width="22" height="22" viewBox="0 0 22 22"><path d="M9 7l4 4-4 4" fill="none" stroke="#fff" stroke-width="1.5"/></svg></div>

<section class="abs guarantee"></section>
<div class="abs guarantee-inner">
  <h2>100% CUSTOMER SATISFACTION GUARANTEED</h2>
  <span class="btn-purple">SHOP NOW</span>
</div>

<h2 class="abs stories-title">Customers</h2>
<div class="abs stories-sub">stories about us</div>
<svg class="abs" style="left:372px;top:3918px" width="20" height="28" viewBox="0 0 20 28"><path d="M14 4L5 14l9 10" fill="none" stroke="#999" stroke-width="2"/></svg>
<svg class="abs" style="left:796px;top:3918px" width="20" height="28" viewBox="0 0 20 28"><path d="M6 4l9 10-9 10" fill="none" stroke="#999" stroke-width="2"/></svg>
<div class="abs avatar" role="img" aria-label="Customer portrait"></div>
<p class="abs testimonial-text">I did my three bathrooms and I couldn't be happier, what a difference the new frames made! Do yourself a favor and frame your mirrors. You'll be happy you did. I would recommend this company.</p>
<div class="abs testimonial-stars stars">★★★★★</div>
<div class="abs testimonial-name">Marla T., Oakridge, GA</div>

<footer class="abs site-footer">
  <div class="footer-col" style="left:58px;width:250px">
    <h4>CONTACT</h4>
    <div class="contact-row"><svg width="12" height="14" viewBox="0 0 12 14" fill="#8a8e98"><path d="M6 0a5 5 0 0 0-5 5c0 4 5 9 5 9s5-5 5-9a5 5 0 0 0-5-5zm0 7a2 2 0 1 1 0-4 2 2 0 0 1 0 4z"/></svg><span>Address<br>2240 Shoreline Ave, Suite 410,<br>Harbor Point, Bayside County, USA</span></div>
    <div style="height:18px"></div>
    <div class="contact-row"><svg width="12" height="12" viewBox="0 0 24 24" fill="#8a8e98"><path d="M6.6 10.8a15 15 0 0 0 6.6 6.6l2.2-2.2c.3-.3.7-.4 1-.2 1.1.4 2.3.6 3.6.6.6 0 1 .4 1 1V20c0 .6-.4 1-1 1C10.6 21 3 13.4 3 4c0-.6.4-1 1-1h3.5c.6 0 1 .4 1 1 0 1.3.2 2.5.6 3.6.1.3 0 .7-.2 1z"/></svg><span>Phone: (555) 014-2290</span></div>
    <div class="contact-row"><svg width="12" height="12" viewBox="0 0 12 12" fill="none" stroke="#8a8e98"><rect x="1" y="2" width="10" height="8"/><path d="M1 2l5 4 5-4"/></svg><span>Fax: (555) 014-2291</span></div>
    <div class="contact-row"><svg width="12" height="12" viewBox="0 0 12 12" fill="none" stroke="#8a8e98"><rect x="1" y="2" width="10" height="8"/><path d="M1 2l5 4 5-4"/></svg><span>Email: <a>info@glassvela.com</a></span></div>
    <div class="contact-row"><svg width="12" height="12" viewBox="0 0 12 12" fill="none" stroke="#8a8e98"><circle cx="6" cy="6" r="5"/><path d="M1 6h10M6 1c3 3 3 7 0 10M6 1c-3 3-3 7 0 10"/></svg><span>Website: <a>www.glassvela.com</a></span></div>
  </div>
  <div class="footer-col" style="left:341px;width:230px">
    <h4>RECENT POSTS</h4>
    <div class="post"><span class="post-dot"></span><p>Easy ways to refresh a tired bathroom mirror<br><span class="date">April 19, 2019</span></p></div>
    <div class="post"><span class="post-dot"></span><p>Choosing a frame finish for your home style<br><span class="date">April 19, 2019</span></p></div>
    <div class="post"><span class="post-dot"></span><p>How to measure your mirror for a perfect fit<br><span class="date">April 19, 2019</span></p></div>
  </div>
  <div class="footer-col" style="left:618px;width:240px">
    <h4>EMAIL US</h4>
    <div class="field">Your name</div>
    <div class="field">Your email</div>
    <div class="field area">Your message</div>
    <div class="send">SEND</div>
  </div>
  <div class="footer-col" style="left:898px;width:230px">
    <h4>FEATURED PRODUCTS</h4>
    <div class="thumbs"><span></span><span></span><span></span><span></span><span></span><span></span><span></span><span></span><span></span></div>
  </div>
</footer>

</body>
</html>
```